All Natural Mosquito Repellent

My company, BrightFern Company has created an all natural mosquito repellent. I already have other all natural products that I have developed and created labels for. I will include a copy of that label so you have something to work from. I will need two labels. One for the front of the bottle and one for the back. The back label will need space for a UPC. The labels need to be 63mm (H) x 39mm (W)

Target Market(s)

Consumers, Organic, People who like natural products

Font styles to use
Other font styles liked:
• A combination of both Serif and Sans Serif

Requirements
Must have
• Use the words Organic, All Natural, Travel size, made in the USA label
Nice to have
• tag line: Don't beat them off. Spray them away.

```html
<!DOCTYPE html>
<html lang="en">
<head>
<meta charset="utf-8">
<title>BrightFern Co. – Mosquito Repellent Labels</title>
<link href="https://fonts.googleapis.com/css2?family=Oswald:wght@500&family=Roboto+Slab:wght@400;600;700&family=Yellowtail&display=swap" rel="stylesheet">
<style>
  :root {
    --canvas: #ffffff;
    --label-bg: #403b36;
    --leaf-green: #37d24f;
    --spray-orange: #ff5405;
    --paper: #ffffff;
    --ink-dark: #403b36;
    --sun-yellow: #f6c744;
    --flag-grey: #d8d8d8;
  }
  * { box-sizing: border-box; margin: 0; padding: 0; }
  html, body { width: 1200px; height: 1200px; overflow: hidden; background: var(--canvas); }
  .sheet { position: relative; width: 1200px; height: 1200px; }

  .label {
    position: absolute; top: 302px; width: 370px; height: 596px;
    background: var(--label-bg);
    box-shadow: 0 14px 22px rgba(0,0,0,0.22);
    overflow: hidden;
  }
  .label--front { left: 187px; }
  .label--back  { left: 643px; }

  .brand-tab { position: absolute; left: 0; top: 0; }
  .brand {
    position: absolute; left: 0; width: 100%;
    text-align: center;
    font-family: "Roboto Slab", serif; font-weight: 700;
    font-size: 15px; letter-spacing: 0.2px;
  }
  .brand__dot { position: absolute; border-radius: 50%; background: var(--sun-yellow); }
  .label--front .brand { top: 84px; color: var(--ink-dark); }
  .label--front .brand__dot { left: 161px; top: 30px; width: 48px; height: 48px; }
  .label--back .brand { top: 132px; color: var(--paper); }
  .label--back .brand__dot { left: 157px; top: 72px; width: 56px; height: 56px; }

  .bug {
    position: absolute; width: 34px; height: 26px; border-radius: 50%;
    background: rgba(255,255,255,0.85);
  }

  .organic {
    position: absolute; left: 0; width: 100%; text-align: center;
    font-family: "Yellowtail", cursive; color: var(--leaf-green);
    line-height: 1;
  }
  .label--front .organic { top: 210px; font-size: 70px; }
  .label--back .organic { top: 390px; font-size: 44px; }
  .leaf { position: absolute; width: 26px; height: 34px; border-radius: 0 100% 0 100%; background: var(--leaf-green); }

  .tagline {
    position: absolute; left: 0; width: 100%; text-align: center;
    font-family: "Oswald", sans-serif; font-weight: 500; color: var(--paper);
    font-size: 21px; line-height: 25px; text-transform: uppercase;
  }
  .tagline--band { top: 302px; height: 25px; background: var(--spray-orange); }
  .tagline--below { top: 327px; }

  .badge {
    position: absolute; top: 399px; width: 74px; height: 74px;
    border: 3px solid var(--leaf-green); border-radius: 50%;
  }
  .badge__core {
    position: absolute; left: 5px; top: 5px; width: 58px; height: 58px; border-radius: 50%;
    display: flex; align-items: center; justify-content: center; text-align: center;
    font-family: "Roboto Slab", serif; font-weight: 700; color: var(--paper);
    font-size: 13px; line-height: 12px;
  }
  .badge--natural { left: 105px; }
  .badge--natural .badge__core { background: var(--leaf-green); }
  .badge--travel { left: 192px; }
  .badge--travel .badge__core { background: var(--spray-orange); }

  .flag { position: absolute; left: 157px; top: 512px; width: 56px; height: 29px; background: var(--flag-grey); }
  .made-in {
    position: absolute; left: 0; top: 553px; width: 100%; text-align: center;
    font-family: "Roboto Slab", serif; font-weight: 600; font-size: 16px;
    color: var(--spray-orange);
  }

  .info-box {
    position: absolute; left: 42px; top: 183px; width: 286px; height: 179px;
    border: 1.5px solid var(--paper);
    display: flex; flex-direction: column; justify-content: center; gap: 14px;
    padding: 0 22px; text-align: center;
    font-family: "Roboto Slab", serif; font-weight: 700; font-size: 11.5px; line-height: 14px;
    color: var(--paper);
  }
</style>
</head>
<body>
<main class="sheet">

  <section class="label label--front" aria-label="Front label">
    <svg class="brand-tab" width="370" height="130" viewBox="0 0 370 130" aria-hidden="true">
      <path d="M80 0 H290 L272 104 Q268 128 244 128 H126 Q102 128 98 104 Z" fill="var(--paper)"/>
    </svg>
    <span class="brand__dot"></span>
    <p class="brand">BrightFern Co.</p>

    <span class="bug" role="img" aria-label="Mosquito illustration" style="left:300px;top:168px;"></span>
    <span class="bug" role="img" aria-label="Mosquito illustration" style="left:145px;top:200px;"></span>
    <span class="bug" role="img" aria-label="Mosquito illustration" style="left:308px;top:386px;"></span>
    <span class="bug" role="img" aria-label="Mosquito illustration" style="left:33px;top:444px;"></span>
    <span class="bug" role="img" aria-label="Mosquito illustration" style="left:35px;top:543px;"></span>
    <span class="bug" role="img" aria-label="Mosquito illustration" style="left:302px;top:533px;"></span>

    <span class="leaf" role="img" aria-label="Leaf sprig" style="left:264px;top:190px;"></span>
    <h1 class="organic">Organic</h1>

    <p class="tagline tagline--band">Don't beat them off.</p>
    <p class="tagline tagline--below">Spray them away.</p>

    <div class="badge badge--natural"><span class="badge__core">All<br>Natural</span></div>
    <div class="badge badge--travel"><span class="badge__core">Travel<br>size</span></div>

    <span class="flag" role="img" aria-label="United States flag"></span>
    <p class="made-in">made in the USA label</p>
  </section>

  <section class="label label--back" aria-label="Back label">
    <span class="brand__dot"></span>
    <p class="brand">BrightFern Co.</p>

    <div class="info-box">
      <p>Lorem ipsum dolor sit amet, consectetuer adipiscing elit, sed diam nonummy nibh euismod tincidunt</p>
      <p>ut laoreet dolore magna aliquam erat volutpat. Ut wisi enim ad minim veniam, quis nostrud exerci tation ullamcorper</p>
    </div>

    <span class="leaf" role="img" aria-label="Leaf sprig" style="left:238px;top:380px;width:20px;height:26px;"></span>
    <p class="organic">Organic</p>
  </section>

</main>
</body>
</html>
```